"Client Services Packet" Folder design for Hair Tissue Mineral Analysis Company

We are looking for an updated folder design which we use mail our new clients information and starter kits for our services. We are looking for a clean and simple design to match our new logo. We would like our logo along with "Client Services Packet" on the front cover with our company information located inside the folder.
Logo file and color palette will be uploaded in the brief.
**Folder will not need the business card cutout shown on current folder**
Address:
4718 E. Corbin Street
Tempe, AZ 85284
Phone:
1-602-418-7362
1-800-736-2915
Fax:
1-602-549-2096
Website:
www.vexmorlab.com
Email:
information@vexmorlab.com
Look and feel
Each slider illustrates characteristics of the customer's brand and the style your logo design should communicate.

```html
<!DOCTYPE html>
<html lang="en">
<head>
<meta charset="utf-8">
<title>Client Services Packet Folder</title>
<link href="https://fonts.googleapis.com/css2?family=Exo+2:wght@400;600;900&display=swap" rel="stylesheet">
<style>
  :root {
    --backdrop: #9eabc5;
    --paper: #f4f4f5;
    --paper-shade: #e9e9eb;
    --navy: #27437f;
    --navy-deep: #1f356b;
    --blue-light: #8fb0d9;
    --orange: #f3923d;
    --ink-dark: #1b2a55;
    --white: #ffffff;
  }
  * { margin: 0; padding: 0; box-sizing: border-box; }
  html, body {
    width: 1200px; height: 652px; overflow: hidden;
    background: var(--backdrop);
    font-family: "Exo 2", sans-serif;
  }
  .canvas { position: relative; width: 1200px; height: 652px; }

  /* Inside spread */
  .inside-spread {
    position: absolute; left: 135px; top: 117px; width: 581px; height: 412px;
    display: flex;
  }
  .inside-panel {
    width: 50%; height: 100%;
    background: linear-gradient(160deg, var(--paper-shade), var(--paper) 60%, #fafafa);
  }
  .inside-panel--left { border-right: 1px solid #dcdce0; }

  .pocket {
    position: absolute; right: 0; bottom: 0; width: 206px; height: 83px;
  }
  .pocket svg { position: absolute; inset: 0; }
  .pocket-info {
    position: absolute; left: 99px; top: 19px;
    display: grid; grid-template-columns: 53px 1fr;
    font-size: 3.6px; line-height: 1.5; color: var(--white);
  }
  .info-block { margin-bottom: 4px; }
  .info-block--phone { margin-top: 8px; }
  .info-label { color: var(--orange); font-weight: 600; }

  /* Front cover */
  .front-cover {
    position: absolute; left: 782px; top: 119px; width: 290px; height: 408px;
    background: linear-gradient(180deg, var(--navy) 0%, var(--navy-deep) 100%);
    overflow: hidden;
  }
  .cover-visual {
    position: absolute; left: 0; top: 0; width: 100%; height: 230px;
    background: radial-gradient(ellipse at 55% 40%, var(--blue-light) 0%, #4a74b8 45%, var(--navy) 85%);
    -webkit-mask-image: linear-gradient(180deg, #000 70%, transparent);
    mask-image: linear-gradient(180deg, #000 70%, transparent);
  }
  .cover-title {
    position: absolute; left: 0; right: 0; top: 246px;
    text-align: center; font-weight: 900; font-size: 20px; line-height: 0.95;
    letter-spacing: -0.2px; text-transform: uppercase;
  }
  .cover-title span { display: block; }
  .title-client { color: var(--ink-dark); }
  .title-services { color: var(--orange); }
  .title-packet { color: var(--white); }
  .cover-brand {
    position: absolute; left: 0; right: 0; top: 376px;
    display: flex; justify-content: center; align-items: center; gap: 5px;
  }
  .brand-mark { width: 7px; height: 7px; border-radius: 50%; background: var(--orange); }
  .brand-name {
    color: var(--blue-light); font-weight: 600; font-size: 9px; letter-spacing: 0.6px;
    text-transform: uppercase; white-space: nowrap;
  }
</style>
</head>
<body>
<main class="canvas">
  <section class="inside-spread" aria-label="Folder inside">
    <div class="inside-panel inside-panel--left"></div>
    <div class="inside-panel inside-panel--right"></div>
    <div class="pocket">
      <svg viewBox="0 0 206 83" width="206" height="83" aria-hidden="true">
        <path d="M0 83 C6 30 45 0 110 0 L206 0 L206 83 Z" fill="var(--navy)"/>
      </svg>
      <div class="pocket-info">
        <div>
          <div class="info-block">
            <div class="info-label">Address:</div>
            <div>4718 E. Corbin Street</div>
            <div>Tempe, AZ 85284</div>
          </div>
          <div class="info-block info-block--phone">
            <div class="info-label">Phone:</div>
            <div>1-602-418-7362</div>
            <div>1-800-736-2915</div>
          </div>
        </div>
        <div>
          <div class="info-block">
            <div class="info-label">Fax:</div>
            <div>1-602-549-2096</div>
          </div>
          <div class="info-block">
            <div class="info-label">Website:</div>
            <div>www.vexmorlab.com</div>
          </div>
          <div class="info-block">
            <div class="info-label">Email:</div>
            <div>information@vexmorlab.com</div>
          </div>
        </div>
      </div>
    </div>
  </section>

  <section class="front-cover" aria-label="Folder front cover">
    <div class="cover-visual" role="img" aria-label="Illustration of blue and orange molecular structures"></div>
    <h1 class="cover-title">
      <span class="title-client">Client</span>
      <span class="title-services">Services</span>
      <span class="title-packet">Packet</span>
    </h1>
    <div class="cover-brand">
      <span class="brand-mark"></span>
      <span class="brand-name">Vexmor Research Labs, Inc.</span>
    </div>
  </section>
</main>
</body>
</html>
```